Webdesign für Personalvermittlung
Zielgruppe
Personalvermittlung
Aufgabenstellung
es soll einladend - nicht zu überladen und natürlich cool und modern sein

```html
<!DOCTYPE html>
<html lang="de">
<head>
<meta charset="utf-8">
<title>Pflegeweg Job – Personalvermittlung</title>
<link href="https://fonts.googleapis.com/css2?family=Bebas+Neue&family=Poppins:wght@400;500;600;700&display=swap" rel="stylesheet">
<style>
:root{
  --green:#3e9e47;--blue:#2aa6df;--orange:#f7931e;--pink:#cf3a6f;--purple:#9a2d8a;
  --ink:#222;--text:#555;--muted:#888;--line:#e4e4e4;--pale:#f1f8fb;--sky:#7ccbea;
}
*{box-sizing:border-box;margin:0;padding:0}
html,body{width:1200px;height:4072px;overflow:hidden}
body{position:relative;font-family:"Poppins",sans-serif;color:var(--ink);background:#fff}
.abs{position:absolute}
a{color:inherit;text-decoration:none}
.topbar{left:100px;right:100px;top:0;height:36px;border-bottom:1px solid var(--line);font-size:11px;display:flex;align-items:center;gap:26px}
.topbar .soc{margin-left:auto;display:flex;gap:14px}
.topbar .soc span{width:12px;height:12px;border-radius:2px;background:#333}
.ic{display:inline-flex;align-items:center;gap:8px}
.logo{display:flex;align-items:center;gap:10px;font-weight:700;font-size:17px;color:#24406e}
.logo i{width:26px;height:26px;border-radius:6px;background:var(--blue)}
.nav{left:100px;right:100px;top:52px;height:34px;display:flex;align-items:center}
.nav ul{display:flex;gap:36px;list-style:none;font-size:13px;margin-left:126px}
.btn{display:inline-flex;align-items:center;justify-content:center;border-radius:30px;font-size:12px;font-weight:500}
.nav .btn{margin-left:auto;background:var(--green);color:#fff;width:174px;height:34px}
.hero h1{left:100px;top:145px;font-family:"Bebas Neue",sans-serif;font-weight:400;font-size:64px;line-height:66px;letter-spacing:1px;color:#2b2b2b}
.hero .sub{left:102px;top:280px;font-size:14px;color:var(--muted)}
.checks{left:100px;top:322px;display:grid;grid-template-columns:240px 200px;row-gap:18px;font-size:15px;list-style:none}
.checks li{display:flex;align-items:center;gap:10px}
.checks svg{width:20px;height:20px}
.hero .para{left:100px;top:454px;width:470px;font-size:15px;line-height:25px;color:var(--muted)}
.hero .b1{left:100px;top:558px;width:136px;height:38px;border:1px solid #999;font-size:11px}
.hero .b2{left:272px;top:568px;font-size:12px}
.photo{left:564px;top:134px;width:538px;height:557px;border-radius:34px;background:linear-gradient(160deg,#dfe7ea,#b9c9d2 55%,#3d7fc0);box-shadow:0 20px 40px rgba(0,0,0,.12)}
.search{left:100px;top:640px;width:695px;height:87px;border-radius:16px;background:#fff;box-shadow:0 12px 30px rgba(0,0,0,.09);display:flex;align-items:center;padding:0 40px;gap:34px}
.search div{font-size:12px;font-weight:500}
.search small{display:block;font-size:11px;color:var(--muted);font-weight:400;margin-bottom:8px}
.search .btn{background:var(--blue);color:#fff;width:134px;height:36px;margin-left:auto}
.stats{left:0;top:790px;width:1200px;height:261px;background:var(--pale)}
.stats h2{position:absolute;left:98px;top:54px;font-size:30px;font-weight:600;line-height:37px;color:#333}
.stats h2 span{color:var(--blue)}
.stats .btn{position:absolute;left:98px;top:185px;width:194px;height:36px;background:var(--blue);color:#fff}
.stat{position:absolute;display:flex;gap:14px}
.stat b{display:block;font-size:24px;font-weight:600;line-height:28px}
.stat small{font-size:14px;color:var(--muted)}
.stat svg{width:40px;height:40px;margin-top:6px}
.expect h2{left:0;right:0;top:1125px;text-align:center;font-size:35px;font-weight:600;line-height:42px;color:#333}
.expect h2 span{color:var(--green)}
.expect .rule{left:425px;top:1221px;width:355px;height:3px;background:var(--green)}
.feat{width:280px;text-align:center}
.feat .icon{margin:0 auto 22px;width:66px;height:44px;position:relative}
.feat .icon::before{content:"";position:absolute;left:26px;top:4px;width:40px;height:40px;border-radius:6px;background:#e3f3e1}
.feat .icon svg{position:relative;width:42px;height:42px}
.feat h3{font-size:24px;font-weight:600;line-height:34px;color:#333;margin-bottom:14px}
.feat p{font-size:12.5px;line-height:18.5px;color:var(--text)}
.reviews{left:0;top:1956px;width:1200px;height:510px;background:#f7f8fa}
.reviews h2{position:absolute;left:96px;top:58px;font-size:34px;font-weight:600}
.reviews h2 span{color:var(--orange)}
.arrow{position:absolute;top:39px;width:72px;height:72px;border-radius:50%;display:flex;align-items:center;justify-content:center}
.card{position:absolute;top:166px;height:268px;border-radius:22px;padding:32px 32px;background:#fff}
.card .who{display:flex;align-items:center;gap:18px;margin-bottom:32px}
.card .av{width:72px;height:72px;border-radius:50%;background:#c9b7a6;flex:none}
.card b{display:block;font-size:22px;font-weight:600}
.card em{font-style:normal;font-size:16px}
.card p{font-size:13px;line-height:26px}
.card.hl{background:var(--orange);color:#fff}
.card.hl p{color:#fde2c3}
.contact h2{left:81px;top:2545px;font-size:34px;font-weight:600}
.contact h2 span{color:var(--pink)}
.contact .intro{left:81px;top:2594px;width:430px;font-size:11.5px;line-height:20px}
.field{position:absolute;height:36px;border-bottom:1px solid #bbb;font-size:13px;color:var(--muted);padding:0 12px;display:flex;align-items:center}
.upload{left:81px;top:2969px;width:457px;height:87px;border:1.5px dashed #bbb;display:flex;align-items:center;justify-content:center;gap:12px;font-size:12px;color:var(--muted)}
.contact .note{left:81px;top:3066px;font-size:10.5px;color:var(--muted)}
.contact .nda{left:81px;top:3107px;font-size:11px;display:flex;gap:10px;align-items:center}
.contact .nda i{width:13px;height:13px;border:1px solid #777}
.submit{left:81px;top:3143px;width:457px;height:43px;background:var(--pink);color:#fff;font-size:12px;font-weight:600;border-radius:6px;display:flex;align-items:center;justify-content:center}
.cinfo{top:3204px;display:flex;gap:14px;font-size:11px;font-weight:600}
.cinfo span{display:block;color:var(--pink);font-weight:500}
.skyblock{left:850px;top:2506px;width:350px;height:760px;background:var(--sky)}
.map{left:591px;top:2547px;width:533px;height:683px;background:linear-gradient(135deg,#eef0ea,#dfe7d8 60%,#d4e4ee)}
.cta{left:0;top:3407px;width:1200px;height:332px;background:var(--pink)}
.cta h2{position:absolute;left:71px;top:78px;width:520px;font-size:34px;line-height:40px;font-weight:600;color:#fff}
.cta .btn{position:absolute;top:232px;height:48px;font-weight:600;font-size:11.5px}
.woman{left:696px;top:3320px;width:430px;height:419px;background:linear-gradient(180deg,#5b3a2e 0%,#f1c21b 45%,#5a8fd6 75%,#e9e6e0 100%);border-radius:200px 200px 0 0}
.foot .logo{position:absolute;left:0;right:0;top:3802px;justify-content:center;font-size:20px}
.foot .logo i{width:36px;height:36px}
.foot ul{position:absolute;left:0;right:0;top:3872px;display:flex;justify-content:center;gap:42px;list-style:none;font-size:12px}
.foot .soc{position:absolute;left:0;right:0;top:3912px;display:flex;justify-content:center;gap:14px}
.foot .soc span{width:34px;height:34px;border-radius:50%;background:var(--purple);display:flex;align-items:center;justify-content:center}
.foot .soc span i{width:12px;height:12px;border-radius:2px;background:#fff}
.foot .rule{position:absolute;left:86px;width:1028px;top:3979px;height:1px;background:var(--purple);opacity:.5}
.foot .copy{position:absolute;left:0;right:0;top:4016px;text-align:center;font-size:12px}
</style>
</head>
<body>

<header>
  <div class="abs topbar">
    <span class="ic"><svg width="12" height="12" viewBox="0 0 24 24"><path fill="var(--green)" d="M6.6 10.8a15 15 0 0 0 6.6 6.6l2.2-2.2c.3-.3.7-.4 1-.2 1.1.4 2.3.6 3.6.6.6 0 1 .4 1 1V20c0 .6-.4 1-1 1A17 17 0 0 1 3 4c0-.6.4-1 1-1h3.5c.6 0 1 .4 1 1 0 1.3.2 2.5.6 3.6.1.3 0 .7-.2 1z"/></svg>07000 123 456 7</span>
    <span class="ic"><svg width="13" height="10" viewBox="0 0 26 20"><rect x="1" y="1" width="24" height="18" rx="2" fill="none" stroke="var(--green)" stroke-width="2"/><path d="M1 2l12 9 12-9" fill="none" stroke="var(--green)" stroke-width="2"/></svg>kontakt@pflegeweg-job.de</span>
    <span class="soc"><span></span><span></span><span></span><span></span></span>
  </div>
  <nav class="abs nav">
    <a class="logo" href="#"><i></i>PFLEGEWEG JOB</a>
    <ul><li>HOME</li><li>WIR BIETEN DIR</li><li>ÜBER UNS</li><li>KONTAKT</li></ul>
    <a class="btn" href="#">Ich will ein Angebot!</a>
  </nav>
</header>

<section class="hero">
  <h1 class="abs">Willkommen bei<br>Pflegeweg-Job.de</h1>
  <p class="abs sub">Wir bieten Ihnen den perfekten Job als Führungskraft!</p>
  <ul class="abs checks">
    <li><svg viewBox="0 0 20 20"><circle cx="10" cy="10" r="10" fill="var(--green)"/><path d="M5.5 10.5l3 3 6-6" fill="none" stroke="#fff" stroke-width="2"/></svg>Wohnbereischsleiter/in</li>
    <li><svg viewBox="0 0 20 20"><circle cx="10" cy="10" r="10" fill="var(--green)"/><path d="M5.5 10.5l3 3 6-6" fill="none" stroke="#fff" stroke-width="2"/></svg>Pflegedienstleiter/in</li>
    <li><svg viewBox="0 0 20 20"><circle cx="10" cy="10" r="10" fill="var(--green)"/><path d="M5.5 10.5l3 3 6-6" fill="none" stroke="#fff" stroke-width="2"/></svg>Stationsleiter/in</li>
    <li><svg viewBox="0 0 20 20"><circle cx="10" cy="10" r="10" fill="var(--green)"/><path d="M5.5 10.5l3 3 6-6" fill="none" stroke="#fff" stroke-width="2"/></svg>OP-Manager/in</li>
    <li><svg viewBox="0 0 20 20"><circle cx="10" cy="10" r="10" fill="var(--green)"/><path d="M5.5 10.5l3 3 6-6" fill="none" stroke="#fff" stroke-width="2"/></svg>Heimleiter/in</li>
    <li><svg viewBox="0 0 20 20"><circle cx="10" cy="10" r="10" fill="var(--green)"/><path d="M5.5 10.5l3 3 6-6" fill="none" stroke="#fff" stroke-width="2"/></svg>Klinikdirektor/in</li>
  </ul>
  <p class="abs para">und willst Dich verändern? Oder möchtest eine Weiterbildung in die Management-Ebene?<br>Dann nimm Kontakt zu uns auf...</p>
  <a class="abs btn b1" href="#">WIR BIETEN DIR</a>
  <a class="abs b2 ic" href="#"><svg width="12" height="14" viewBox="0 0 12 14"><path d="M0 0l12 7-12 7z" fill="#222"/></svg>&nbsp; Watch Video</a>
  <div class="abs photo" role="img" aria-label="Foto: Pflegekraft in blauer Kleidung mit Tablet, im Hintergrund Ärzte im Gespräch"></div>
  <div class="abs search">
    <div><small>Location</small><span class="ic"><svg width="10" height="12" viewBox="0 0 10 14"><path d="M5 0a5 5 0 0 0-5 5c0 4 5 9 5 9s5-5 5-9a5 5 0 0 0-5-5z" fill="none" stroke="var(--green)" stroke-width="1.5"/></svg>Choose Location</span></div>
    <div><small>Your Contact Details</small><span class="ic"><svg width="8" height="12" viewBox="0 0 8 12"><rect x=".75" y=".75" width="6.5" height="10.5" rx="1" fill="none" stroke="var(--green)" stroke-width="1.5"/></svg>Mobile No.</span></div>
    <div><small>Select Position</small><span class="ic"><svg width="11" height="11" viewBox="0 0 12 12"><rect x=".75" y="1.75" width="10.5" height="9.5" fill="none" stroke="var(--green)" stroke-width="1.5"/></svg>Heimleiter/in &nbsp;⌄</span></div>
    <a class="btn" href="#">Upload A Resume</a>
  </div>
</section>

<section class="abs stats">
  <h2>Dein nächster<br><span>Karriereschritt im<br>Pflegeberuf!</span></h2>
  <a class="btn" href="#">Ich will ein Angebot!</a>
  <div class="stat" style="left:629px;top:58px"><svg viewBox="0 0 40 40" fill="none" stroke="var(--green)" stroke-width="2.5"><circle cx="14" cy="14" r="7"/><circle cx="27" cy="14" r="7"/><path d="M2 34c2-8 8-11 12-11s10 3 12 11M20 23c2-1 4-1 7-1 4 0 10 3 12 11"/></svg><div><b style="color:var(--green)">15 Years</b><small>Erfahrung</small></div></div>
  <div class="stat" style="left:874px;top:58px"><svg viewBox="0 0 40 40" fill="none" stroke="var(--orange)" stroke-width="2"><circle cx="20" cy="8" r="5"/><circle cx="9" cy="20" r="4"/><circle cx="31" cy="20" r="4"/><path d="M12 34c0-8 4-14 8-14s8 6 8 14"/></svg><div><b style="color:var(--orange)">20k+</b><small>zufriedene Kunden</small></div></div>
  <div class="stat" style="left:629px;top:153px"><svg viewBox="0 0 40 40" fill="var(--blue)"><circle cx="18" cy="10" r="5"/><path d="M8 36V26c0-5 4-9 10-9s10 4 10 9v10z"/></svg><div><b style="color:var(--blue)">15k+</b><small>Platzierung</small></div></div>
  <div class="stat" style="left:874px;top:153px"><svg viewBox="0 0 40 40" fill="none" stroke="var(--purple)" stroke-width="2.5"><rect x="3" y="9" width="34" height="24" rx="4"/><path d="M3 17h34M26 26h6"/></svg><div><b style="color:var(--purple)">17k+</b><small>Vorstellungsgespräche</small></div></div>
</section>

<section class="expect">
  <h2 class="abs">Was darfst Du von<br><span>PFLEGEWEG-JOB.de erwarten?</span></h2>
  <div class="abs rule"></div>
  <div class="abs feat" style="left:80px;top:1292px"><div class="icon"><svg viewBox="0 0 42 42" fill="none" stroke="var(--green)" stroke-width="2"><rect x="6" y="12" width="30" height="22" rx="3"/><path d="M16 12V8h10v4"/></svg></div><h3>Zugriff auf mehr<br>Stellen</h3><p>In Zusammenarbeit mit Einrichtungen und Kliniken erhalten unsere Kandidaten einen zugesicherten Bonus in Höhe von 750 EUR für das Vertrauen bei Ihrem Jobwechsel in pflegeweg-Job.de</p></div>
  <div class="abs feat" style="left:455px;top:1292px"><div class="icon"><svg viewBox="0 0 42 42" fill="none" stroke="var(--green)" stroke-width="2"><rect x="9" y="5" width="24" height="32" rx="2"/><path d="M14 14h14M14 20h14M14 26h9"/></svg></div><h3>Verspricht<br>Arbeitsvertrag</h3><p>Du stellst Bedingungen an deinen neuen Arbeitgeber? – dann sorgen wir gemeinsam dafür, dass Du diese auch im Arbeitsvertrag findest – zu Deiner Sicherheit. Nichts ist schlimmer, als leere Versprechungen!</p></div>
  <div class="abs feat" style="left:831px;top:1292px"><div class="icon"><svg viewBox="0 0 42 42" fill="none" stroke="var(--green)" stroke-width="2"><circle cx="21" cy="16" r="9"/><path d="M8 38c2-8 7-12 13-12s11 4 13 12"/></svg></div><h3>Dauerhafte<br>Betreuung</h3><p>Dein neuer Arbeitgeber hält nicht was er verspricht? Keine Sorge, wir werden für Dich sofort wieder aktiv und bieten Dir schnell neue Möglichkeiten an – ohne dass Du erneut Bewerbungen versenden musst! Ein Anruf oder eine Email genügt!</p></div>
  <div class="abs feat" style="left:80px;top:1613px"><div class="icon"><svg viewBox="0 0 42 42" fill="none" stroke="var(--green)" stroke-width="2"><circle cx="21" cy="15" r="8"/><path d="M7 38c2-8 7-12 14-12s12 4 14 12"/><path d="M12 12h18"/></svg></div><h3>Anonymität</h3><p>Wir erstellen ein Profil Deiner Kenntnisse und Fähigkeiten sowie Deiner Berufserfahrung. Weder Dein Name, noch Deine Vorarbeitgeber tauchen im ersten Schritt auf. Erst wenn eine Einrichtung oder Klinik daran Interesse zeigt, entscheiden wir gemeinsam, wie es weitergeht!</p></div>
  <div class="abs feat" style="left:455px;top:1613px"><div class="icon"><svg viewBox="0 0 42 42" fill="none" stroke="var(--green)" stroke-width="2"><circle cx="21" cy="21" r="15"/><path d="M13 22l6 6 10-12"/></svg></div><h3>Keine Zeitarbeit</h3><p>Wir vermitteln ausschließlich in Festanstellungen direkt bei Kliniken oder Einrichtungen. Wir können Dir jedoch wertvolle Tipps geben, sollte Zeitarbeit für Dich in Frage kommen ...WIR KENNEN UNS AUS!</p></div>
  <div class="abs feat" style="left:831px;top:1613px"><div class="icon"><svg viewBox="0 0 42 42" fill="none" stroke="var(--green)" stroke-width="2"><circle cx="21" cy="21" r="15"/><circle cx="21" cy="21" r="10"/></svg></div><h3>100% kostenfrei</h3><p>Unsere Dienstleistung ist für Dich als Bewerber 100% kostenfrei! Es gibt auch garantiert keine versteckten Kosten!</p></div>
</section>

<section class="abs reviews">
  <h2>Was Unsere Kunden <span>Über Uns Sagen</span></h2>
  <div class="arrow" style="left:938px;background:#fff"><svg width="22" height="14" viewBox="0 0 22 14" fill="none" stroke="#bbb" stroke-width="2"><path d="M21 7H2M8 1L2 7l6 6"/></svg></div>
  <div class="arrow" style="left:1026px;background:var(--orange)"><svg width="22" height="14" viewBox="0 0 22 14" fill="none" stroke="#fff" stroke-width="2"><path d="M1 7h19M14 1l6 6-6 6"/></svg></div>
  <div class="card hl" style="left:96px;width:427px"><div class="who"><div class="av" role="img" aria-label="Porträtfoto der Kundin"></div><div><b>Lena Hartmann</b><em>Heimleiter/In</em></div></div><p style="line-height:23px">Meine Vision wurde mühelos lebendig. Ihre Mischung aus lockeren und professionellen Herangehensweisen machte den Prozess zu einem Kinderspiel. Die Kreativität floss und die Ergebnisse übertrafen meine Erwartungen.</p></div>
  <div class="card" style="left:541px;width:425px"><div class="who"><div class="av" role="img" aria-label="Porträtfoto der Kundin"></div><div><b>Jonas Berger</b><em>OP-Manager/In</em></div></div><p>Ich habe die digitale Expertise gefunden, die ich brauchte. Ihre kreativ-berufliche Balance übertraf alle Erwartungen. Freundliche Interaktionen, außergewöhnliche Ergebnisse. Für digitale Verzauberung muss es Lumen sein!</p></div>
  <div class="card" style="left:983px;width:425px"><div class="who"><div class="av" role="img" aria-label="Porträtfoto des Kunden"></div><div><b>Tobias Krämer</b><em>Stationsleiter/In</em></div></div><p>Lumen bringt es wirklich auf den Punkt. Brillanz, zugänglicher Stil. Sie suchen – Kunst trifft auf Strategie – von dem, was sie erreicht haben.</p></div>
</section>

<section class="contact">
  <div class="abs skyblock"></div>
  <div class="abs map" role="img" aria-label="Stadtplan mit markiertem Firmenstandort"></div>
  <h2 class="abs">Get In <span>Touch</span></h2>
  <p class="abs intro">Enim tempor eget pharetra facilisis sed maecenas adipiscing. Eu leo molestie vel, ornare non id blandit netus.</p>
  <div class="field" style="left:81px;top:2657px;width:457px">Contact name</div>
  <div class="field" style="left:81px;top:2710px;width:457px">Street</div>
  <div class="field" style="left:81px;top:2762px;width:296px">City</div>
  <div class="field" style="left:396px;top:2762px;width:142px">Postcode</div>
  <div class="field" style="left:81px;top:2806px;width:457px">Contact Phone</div>
  <div class="field" style="left:81px;top:2860px;width:457px">E-mail</div>
  <div class="field" style="left:81px;top:2912px;width:457px">Let's talk about your idea</div>
  <div class="abs upload"><svg width="16" height="16" viewBox="0 0 16 16" fill="none" stroke="#999" stroke-width="1.5"><path d="M8 11V2M4 6l4-4 4 4M1 11v4h14v-4"/></svg>Upload Additional file</div>
  <p class="abs note">Attach file. File size of your documents should not exceed 10MB</p>
  <label class="abs nda"><i></i>I want to protect my data by signing an NDA</label>
  <a class="abs submit" href="#">SUBMIT</a>
  <div class="abs cinfo" style="left:74px"><svg width="22" height="22" viewBox="0 0 24 24" fill="none" stroke="#222" stroke-width="1.5"><path d="M6.6 10.8a15 15 0 0 0 6.6 6.6l2.2-2.2c.3-.3.7-.4 1-.2 1.1.4 2.3.6 3.6.6.6 0 1 .4 1 1V20c0 .6-.4 1-1 1A17 17 0 0 1 3 4c0-.6.4-1 1-1h3.5c.6 0 1 .4 1 1 0 1.3.2 2.5.6 3.6.1.3 0 .7-.2 1z"/></svg><div>Phone<span>07000 123 456 7</span></div></div>
  <div class="abs cinfo" style="left:286px"><svg width="22" height="20" viewBox="0 0 24 22" fill="none" stroke="#222" stroke-width="1.5"><rect x="1" y="5" width="22" height="16" rx="1"/><path d="M1 6l11 8 11-8M5 5V1h14v4"/></svg><div>E-MAIL<span style="text-decoration:underline">kontakt@pflegeweg-job.de</span></div></div>
</section>

<section class="abs cta">
  <h2>Senden Sie noch heute Ihren Lebenslauf. Holen Sie sich morgen Ihren Job.</h2>
  <a class="btn" href="#" style="left:71px;width:162px;background:#fff;color:var(--pink)">GET STARTED &nbsp;⟶</a>
  <a class="btn" href="#" style="left:250px;width:142px;border:1.5px solid #fff;color:#fff">BOOK A CALL</a>
</section>
<div class="abs woman" role="img" aria-label="Foto: Frau sitzt im Schneidersitz mit Laptop"></div>

<footer class="foot">
  <div class="logo"><i></i>PFLEGEWEG JOB</div>
  <ul><li>HOME</li><li>WIR BIETEN DIR</li><li>ÜBER UNS</li><li>KONTAKT</li></ul>
  <div class="soc"><span><i></i></span><span><i></i></span><span><i></i></span><span><i></i></span></div>
  <div class="rule"></div>
  <p class="copy">Copyright pflegeweg</p>
</footer>

</body>
</html>
```